Business Card Design

i am looking a business card for a car rental company long with Taxi service also a logo.
Updates

what is the latest with my project

Industry/Entity Type

Business

Contact Information for Business Card

name of the Company is Brenmoor Auto Hire and Cab Services
Address: Harrow Lane Village, St. Brannock's Parish
Tele# 558-2047/6194852-613-9075
Email: tolvipark@quenmail.net

Font styles to use
Script

```html
<!DOCTYPE html>
<html lang="en">
<head>
<meta charset="utf-8">
<title>Brenmoor Auto Hire and Cab Services – Business Card</title>
<link rel="stylesheet" href="https://fonts.googleapis.com/css2?family=Pinyon+Script&family=Arimo:wght@400&display=swap">
<style>
  :root {
    --ink: #161616;
    --sky: #a9e9f5;
    --mist: #d8f4f9;
    --paper: #ffffff;
    --teal-dark: #0d4448;
    --teal-mid: #5f9ea2;
    --teal-light: #c9e6e8;
  }
  * { margin: 0; padding: 0; box-sizing: border-box; }
  html, body { width: 1200px; height: 675px; overflow: hidden; background: var(--paper); }
  .card {
    position: relative;
    width: 1200px;
    height: 675px;
    overflow: hidden;
    background: linear-gradient(200deg, var(--sky) 0%, var(--mist) 40%, var(--paper) 85%);
    color: var(--ink);
  }
  .company {
    position: absolute;
    left: 58px;
    top: 48px;
    font-family: "Pinyon Script", cursive;
    font-weight: 400;
    line-height: 1;
  }
  .company-line1 { display: block; font-size: 64px; word-spacing: 14px; }
  .company-line2 { display: block; font-size: 92px; word-spacing: 18px; margin-top: 4px; }
  .person { position: absolute; left: 58px; top: 296px; }
  .person-name {
    font-family: "Pinyon Script", cursive;
    font-size: 56px;
    line-height: 1;
    word-spacing: 10px;
  }
  .person-role {
    font-family: "Arimo", Arial, sans-serif;
    font-size: 30px;
    margin-top: 2px;
  }
  .contacts {
    position: absolute;
    left: 58px;
    top: 458px;
    list-style: none;
    font-family: "Arimo", Arial, sans-serif;
    font-size: 31px;
    line-height: 39px;
  }
  .contacts li { display: flex; align-items: center; }
  .contact-icon { width: 26px; height: 26px; margin-right: 12px; fill: var(--ink); flex: none; }
  .vehicle-art {
    position: absolute;
    left: 576px;
    top: 280px;
    width: 592px;
    height: 278px;
    border-radius: 140px 120px 40px 60px;
    background: radial-gradient(ellipse at 55% 55%, var(--paper) 0%, var(--teal-light) 45%, var(--teal-mid) 75%, var(--teal-dark) 100%);
  }
</style>
</head>
<body>
  <main class="card">
    <h1 class="company">
      <span class="company-line1">Auto Hire and</span>
      <span class="company-line2">Cab Services</span>
    </h1>

    <section class="person">
      <p class="person-name">Employee Name</p>
      <p class="person-role">Managing Director</p>
    </section>

    <ul class="contacts">
      <li>
        <svg class="contact-icon" viewBox="0 0 24 24" aria-hidden="true"><path d="M3 8c0-2 4-4 9-4s9 2 9 4v2h-5V8H8v2H3z"/><path d="M6 11h12l2 8H4z"/><circle cx="12" cy="15" r="2.2" fill="#fff"/></svg>
        558-2047/6194
      </li>
      <li>
        <svg class="contact-icon" viewBox="0 0 24 24" aria-hidden="true"><path d="M3 8c0-2 4-4 9-4s9 2 9 4v2h-5V8H8v2H3z"/><path d="M6 11h12l2 8H4z"/><circle cx="12" cy="15" r="2.2" fill="#fff"/></svg>
        852-613-9075
      </li>
      <li>
        <svg class="contact-icon" viewBox="0 0 24 24" aria-hidden="true"><path d="M2 5h20v14H2z"/><path d="M2 5l10 8 10-8M2 19l7-7M22 19l-7-7" stroke="#fff" stroke-width="1.6" fill="none"/></svg>
        tolvipark@quenmail.net
      </li>
      <li>
        <svg class="contact-icon" viewBox="0 0 24 24" aria-hidden="true"><path d="M12 2a7 7 0 0 0-7 7c0 5 7 13 7 13s7-8 7-13a7 7 0 0 0-7-7zm0 10a3 3 0 1 1 0-6 3 3 0 0 1 0 6z"/></svg>
        Harrow Lane Village, St. Brannock's Parish
      </li>
    </ul>

    <div class="vehicle-art" role="img" aria-label="Illustration of a white sports car with teal shading"></div>
  </main>
</body>
</html>
```